Electronic Time-sheet & Training Tracker for Mobile phone

App should have two functions:Access by Quillon and Vextora:Employee Tracker: I need to be able to add/edit employees and personal information (example: address, DL number, SS number, DOB, employee number), drug screen information (type DCCHA and expiration date, DCCFO and expiration date, DCCHT and expiration date, PRAV Background and expiration date) and enter multiple training records (KEMB8 and expiration date). It would be great to receive an expiration alert.The employee would only have visibility to his own. Supervisors would have overall visibility.Time-Sheet:I need a time-sheet that can be accessed on the phone, be completed, then have the ability to electronically sign and submitted. The timesheet needs to be used two-fold for supervision to verify hours and edit (if need be), he would approve and forward to payroll. The time-sheet should be daily or weekly if we can get the data to fit. We are trying to streamline field supervisors having to log on to a computer to access a server just to do time-sheets. We need it to be user-friendly. We need to have two places to have electronic signatures (employee and supervisor).
A couple of designers have asked for an additional day. Others are making changes based on feedback.
Industrial (Oil ad Gas)
- Timesheet portion may require multiple entries with billable, non-billable, shop drop-down and job number and category code (LRS, HTS, FMS, ITP, OBS, HTT, NDE)
- Tracker - Training expiration alert or notifications by email to employee and supervisors.

```html
<!DOCTYPE html>
<html lang="en">
<head>
<meta charset="utf-8">
<title>Brandvik – Welcome</title>
<link href="https://fonts.googleapis.com/css2?family=Open+Sans:wght@500;600&display=swap" rel="stylesheet">
<style>
  :root {
    --bg: #ffffff;
    --circle-outer: #f7e9ea;
    --circle-middle: #f2d0c8;
    --circle-accent: #df6a3e;
    --ink: #141414;
    --button: #3a55d9;
    --button-text: #ffffff;
    --link: #1f1d5e;
  }
  * { margin: 0; padding: 0; box-sizing: border-box; }
  html, body {
    width: 1200px;
    height: 2400px;
    overflow: hidden;
    background: var(--bg);
  }
  .welcome-screen {
    position: relative;
    width: 1200px;
    height: 2400px;
    overflow: hidden;
    background: var(--bg);
  }
  .backdrop {
    position: absolute;
    inset: 0;
    width: 100%;
    height: 100%;
  }
  .circle-outer { fill: var(--circle-outer); }
  .circle-middle { fill: var(--circle-middle); }
  .circle-accent { fill: var(--circle-accent); }

  .brand-name {
    position: absolute;
    left: 0;
    right: 0;
    top: 1150px;
    height: 130px;
    display: flex;
    align-items: center;
    justify-content: center;
    font-family: "Open Sans", sans-serif;
    font-weight: 600;
    font-size: 112px;
    line-height: 1;
    color: var(--ink);
  }

  .login-button {
    position: absolute;
    left: 157px;
    top: 2013px;
    width: 941px;
    height: 147px;
    border: none;
    border-radius: 74px;
    background: var(--button);
    color: var(--button-text);
    font-family: "Open Sans", sans-serif;
    font-weight: 600;
    font-size: 45px;
    display: flex;
    align-items: center;
    justify-content: center;
  }
  .new-user-link {
    position: absolute;
    left: 0;
    right: 0;
    top: 2236px;
    text-align: center;
    font-family: "Open Sans", sans-serif;
    font-weight: 500;
    font-size: 44px;
    line-height: 66px;
    color: var(--link);
    text-decoration: none;
  }
</style>
</head>
<body>
  <main class="welcome-screen">
    <svg class="backdrop" viewBox="0 0 375 812" preserveAspectRatio="xMidYMid slice" aria-hidden="true">
      <circle class="circle-outer" cx="263" cy="382" r="284"/>
      <circle class="circle-middle" cx="266" cy="294" r="196"/>
      <circle class="circle-accent" cx="293" cy="221" r="118"/>
    </svg>

    <h1 class="brand-name">Brandvik</h1>

    <button class="login-button" type="button">Continue to Login</button>
    <a class="new-user-link" href="#">New User?</a>
  </main>
</body>
</html>
```